Rollup banner and Logo design

I need to update my roll-up banner design from the attached to something nicer :-).
The product is SAAS software
Text attached
We're also open to improving the logo which at the moment is just text

Software

```html
<!DOCTYPE html>
<html lang="en">
<head>
<meta charset="utf-8">
<title>Translation Project Management – Rollup Banner</title>
<link rel="stylesheet" href="https://fonts.googleapis.com/css2?family=Montserrat:ital,wght@0,600;0,700;0,800;1,700;1,800&family=Open+Sans:wght@400;600&display=swap">
<style>
  :root {
    --navy: #2a3d58;
    --navy-deep: #1f2f45;
    --red: #b3262c;
    --red-light: #c9373b;
    --red-deep: #871a1f;
    --white: #ffffff;
    --ink-soft: #f3dede;
  }
  html, body {
    margin: 0;
    padding: 0;
    width: 1200px;
    height: 3103px;
    overflow: hidden;
    background: var(--white);
  }
  .banner {
    position: relative;
    width: 1200px;
    height: 3103px;
    overflow: hidden;
    background: var(--white);
    font-family: "Open Sans", Arial, sans-serif;
  }
  .backdrop {
    position: absolute;
    inset: 0;
    width: 1200px;
    height: 3103px;
  }
  .title {
    position: absolute;
    left: 0;
    width: 1200px;
    text-align: center;
    color: var(--navy);
    font-family: "Montserrat", Arial, sans-serif;
    margin: 0;
  }
  .title-top {
    top: 118px;
    font-size: 60px;
    font-weight: 700;
    letter-spacing: 8px;
  }
  .title-main {
    top: 196px;
    font-size: 92px;
    font-weight: 700;
    letter-spacing: 9px;
  }
  .tagline {
    position: absolute;
    top: 400px;
    left: 0;
    width: 1200px;
    height: 152px;
    line-height: 152px;
    margin: 0;
    text-align: center;
    color: var(--white);
    font-family: "Montserrat", Arial, sans-serif;
    font-size: 124px;
    font-weight: 700;
    letter-spacing: 6px;
  }
  .tagline em {
    font-style: italic;
    font-weight: 800;
  }
  .features {
    position: absolute;
    top: 790px;
    left: 0;
    width: 1200px;
    margin: 0;
    padding: 0;
    list-style: none;
  }
  .feature {
    position: absolute;
    left: 0;
    width: 1200px;
  }
  .feature-arrow {
    position: absolute;
    left: 110px;
    top: 0;
    width: 58px;
    height: 66px;
  }
  .feature-heading {
    margin: 0 0 0 231px;
    color: var(--white);
    font-family: "Montserrat", Arial, sans-serif;
    font-size: 47px;
    font-weight: 700;
    letter-spacing: 7px;
    line-height: 62px;
  }
  .feature-text {
    margin: 10px 0 0 231px;
    width: 780px;
    color: var(--ink-soft);
    font-size: 39px;
    letter-spacing: 2.5px;
    line-height: 52px;
  }
  .brand {
    position: absolute;
    top: 2385px;
    left: 640px;
    width: 520px;
    text-align: center;
  }
  .brand-dot {
    display: block;
    width: 260px;
    height: 260px;
    margin: 0 auto 30px;
    border-radius: 50%;
    background: var(--navy);
  }
  .brand-name {
    margin: 0;
    color: var(--red);
    font-family: "Montserrat", Arial, sans-serif;
    font-size: 66px;
    font-weight: 800;
    letter-spacing: 3px;
    line-height: 1;
    white-space: nowrap;
  }
  .footer {
    position: absolute;
    left: 0;
    top: 2810px;
    width: 1200px;
    height: 293px;
    background: var(--navy);
    text-align: center;
    color: var(--white);
  }
  .footer-url {
    margin: 68px 0 0;
    font-family: "Montserrat", Arial, sans-serif;
    font-size: 60px;
    font-weight: 700;
    letter-spacing: 3px;
  }
  .footer-note {
    margin: 18px 0 0;
    font-family: "Montserrat", Arial, sans-serif;
    font-size: 38px;
    font-weight: 600;
    letter-spacing: 4px;
  }
</style>
</head>
<body>
<main class="banner">
  <svg class="backdrop" viewBox="0 0 1200 3103" aria-hidden="true">
    <defs>
      <radialGradient id="redGlow" cx="0.45" cy="0.4" r="0.75">
        <stop offset="0" stop-color="#c9373b"/>
        <stop offset="0.7" stop-color="#b3262c"/>
        <stop offset="1" stop-color="#8f1c21"/>
      </radialGradient>
    </defs>
    <rect x="0" y="397" width="1200" height="155" fill="#2a3d58"/>
    <path d="M0,560 Q600,600 1200,566 L1200,580 Q600,622 0,576 Z" fill="#2a3d58"/>
    <path d="M0,600 Q600,640 1200,598 L1200,2000 C900,2230 420,2290 0,2248 Z" fill="url(#redGlow)"/>
    <path d="M0,600 Q600,640 1200,598 L1200,616 Q600,660 0,618 Z" fill="#871a1f"/>
    <path d="M1200,2000 C900,2230 420,2290 0,2248 L0,2300 C460,2340 940,2240 1200,2060 Z" fill="#2a3d58"/>
  </svg>

  <h1 class="title title-top">TRANSLATION PROJECT</h1>
  <p class="title title-main">MANAGEMENT</p>
  <p class="tagline">THE <em>EASY</em> WAY</p>

  <ul class="features">
    <li class="feature" style="top:0">
      <svg class="feature-arrow" viewBox="0 0 58 66"><path d="M0,0 L58,33 L0,66 L16,33 Z" fill="#ffffff"/></svg>
      <h2 class="feature-heading">MANAGE TRANSLATION<br>PROJECTS EASILY</h2>
      <p class="feature-text">Simple workflows minimise the amount ot time you spend on projects</p>
    </li>
    <li class="feature" style="top:370px">
      <svg class="feature-arrow" viewBox="0 0 58 66"><path d="M0,0 L58,33 L0,66 L16,33 Z" fill="#ffffff"/></svg>
      <h2 class="feature-heading">FINANCIAL MANAGEMENT<br>&amp; REPORTING</h2>
      <p class="feature-text">Financial dashboards &amp; powerful reports show how your business is doing</p>
    </li>
    <li class="feature" style="top:735px">
      <svg class="feature-arrow" viewBox="0 0 58 66"><path d="M0,0 L58,33 L0,66 L16,33 Z" fill="#ffffff"/></svg>
      <h2 class="feature-heading">CLIENT &amp; RESOURCE<br>PORTALS</h2>
      <p class="feature-text">Clients &amp; Resources can see their projects &amp; paperwork in real time</p>
    </li>
    <li class="feature" style="top:1090px">
      <svg class="feature-arrow" viewBox="0 0 58 66"><path d="M0,0 L58,33 L0,66 L16,33 Z" fill="#ffffff"/></svg>
      <h2 class="feature-heading">COLLABORATION &amp;<br>TERM MANAGEMENT</h2>
      <p class="feature-text">Real time discussion &amp; term management tools improve translation quality</p>
    </li>
  </ul>

  <div class="brand">
    <span class="brand-dot"></span>
    <p class="brand-name">LINGOFLOW</p>
  </div>

  <footer class="footer">
    <p class="footer-url">www.lingoflowhub.com</p>
    <p class="footer-note">A product of Meridian Works LLP</p>
  </footer>
</main>
</body>
</html>
```